Glenmoor Vale Executive Development Workshop Series

* Had error in first version of MS Word doc and have re-uploaded - twelve subject areas, not nine *
I'd like a flyer to print to hand out and post on my website glenmoorvale.com to advertise a workshop series I'm launching. I'd like it to build strongly on the wonderful logo you did and Scottish theme...and to have the same "feel" as my website. glenmoorvale.com
It should be 8.5x11, single sided. Not sure if I should use full color glossy or two-color on nice paper. Regardless, I will most likely have it done on a color copier and will not put it on a printing press.
I have typed up a document with all the information in a MS Word file, but need you to lay it out in an aesthetically pleasing way. I have attached that MS Word file.
I am also attaching a handful of similar flyer documents from other non-competing coaches in my network. I think they all have their merits, but leave me under-whelmed.
I'm also attaching a picture of me and some pictures of Scotland my parents took about 10 years ago. I'm reluctantly open to stock photos, just not too obvious or hackneyed (if that word can be applied to pictures as well as expressions).
Lastly, this workshop series will be an ongoing thing, so I'd like to be able to make minor edits myself with things like new dates or topics.
Thank you!
Target Market(s)
Small business owners and emerging leaders with large companies
Colors
Designer to choose colors to be used in the design.
Requirements
Should not have
- Obviously stock photos

```html
<!DOCTYPE html>
<html lang="en">
<head>
<meta charset="utf-8">
<title>Glenmoor Vale Executive Development Workshop Series</title>
<link rel="stylesheet" href="https://fonts.googleapis.com/css2?family=Crimson+Pro:wght@400;700&family=Mulish:wght@400;600&display=swap">
<style>
:root{
  --stage:#3b3b3b;
  --paper:#ffffff;
  --ink:#3a3a3a;
  --olive:#3b4226;
  --olive-text:#3d4427;
  --sage:#c2d19a;
  --sage-dark:#9fb36f;
  --badge:#d8d8d3;
  --muted:#d9d9d9;
}
*{box-sizing:border-box;margin:0;padding:0}
html,body{width:1029px;height:1200px;overflow:hidden;background:var(--stage)}
body{font-family:"Mulish",Arial,sans-serif;color:var(--ink)}
.flyer{position:absolute;left:90px;top:50px;width:850px;height:1100px;background:var(--paper);overflow:hidden}
.hero{position:absolute;left:0;top:0;width:850px;height:410px;
  background:linear-gradient(180deg,#0f0f0f 0,#2a2a2a 50px,#4f5140 120px,#6b6a4c 240px,#7a6a48 330px,#6a5a3c 410px)}
.hero-photo{position:absolute;left:0;top:0;width:850px;height:410px}
.portrait{position:absolute;left:80px;top:60px;width:200px;height:290px;
  background:linear-gradient(180deg,rgba(170,155,140,.55) 0,rgba(120,105,92,.6) 60%,rgba(80,72,62,.6) 100%)}
.series-title{position:absolute;left:0;top:18px;width:850px;text-align:center;font-family:"Crimson Pro",Georgia,serif;font-size:25px;font-weight:400;color:#fff;letter-spacing:.2px}
.series-title b{font-weight:700}
.coach-name{position:absolute;left:426px;top:160px;font-family:"Crimson Pro",Georgia,serif;font-size:42px;color:#fff;font-weight:400}
.coach-rule{position:absolute;left:426px;top:211px;width:357px;height:2px;background:var(--muted)}
.coach-title{position:absolute;left:426px;top:219px;font-size:18px;color:var(--muted)}
.tagline{position:absolute;left:426px;top:257px;width:361px;font-size:17px;line-height:22px;color:#fff;text-align:justify}
.swoosh{position:absolute;left:0;top:300px;width:850px;height:140px}
.intro{position:absolute;left:24px;top:404px;width:360px;font-size:13px;line-height:16.5px;color:#555}
.intro p+p{margin-top:16px}
.includes{position:absolute;left:24px;top:570px;width:370px;border-top:1px solid var(--sage)}
.includes h2{font-size:16px;font-weight:600;color:var(--olive-text);margin:9px 0 12px}
.include-item{position:relative;padding-left:22px;font-size:13px;line-height:16.5px;color:#555;text-align:justify;margin-bottom:8px}
.include-item::before{content:"";position:absolute;left:2px;top:3px;width:11px;height:11px;border-radius:50%;background:var(--sage)}
.include-item strong{display:block;font-weight:400;color:var(--olive-text)}
.fine-print{position:absolute;left:24px;top:780px;width:370px;border-top:1px solid var(--sage);padding:11px 10px 0;font-size:11.5px;line-height:13.5px;color:#555;text-align:justify}
.fine-print p+p{margin-top:14px}
.fine-print .venue{color:var(--olive-text)}
.price{position:absolute;left:34px;top:932px;width:350px;font-size:16px;line-height:20px;font-weight:600;color:var(--olive-text)}
.schedule{position:absolute;left:434px;top:451px;width:384px;list-style:none}
.schedule li{position:relative;padding-left:12px;margin-bottom:4px}
.schedule li::before{content:"›";position:absolute;left:0;top:-3px;font-size:16px;font-weight:600;color:var(--olive)}
.session{display:block;font-size:14px;line-height:16px;color:var(--olive-text)}
.session b{font-weight:600}
.summary{display:block;font-size:12.5px;line-height:15px;color:#333}
.member-badge{position:absolute;left:780px;top:452px;width:44px;height:44px;border-radius:50%;background:var(--badge)}
.register{position:absolute;left:425px;top:929px;width:398px;height:50px;border:2px solid var(--olive);padding-top:4px;text-align:center;font-size:16px;line-height:19px;color:var(--olive-text)}
.register b{font-weight:600}
.footer-band{position:absolute;left:0;top:995px;width:850px;height:8px;background:var(--sage)}
.footer{position:absolute;left:0;top:1003px;width:850px;height:97px;background:var(--olive);color:#e8ead8}
.footer-name{position:absolute;left:31px;top:17px;font-family:"Crimson Pro",Georgia,serif;font-size:15px}
.footer-name b{font-weight:700}
.contact{position:absolute;left:31px;top:42px;list-style:none;font-size:12.5px;line-height:18px}
.contact li{display:flex;align-items:center;gap:7px}
.contact svg{width:9px;height:9px;fill:#e8ead8}
.brand{position:absolute;right:32px;top:36px;display:flex;align-items:center;gap:9px;font-size:22px;color:#e8ead8}
.brand-dot{width:12px;height:12px;border-radius:50%;background:#e8ead8}
</style>
</head>
<body>
<main class="flyer">
  <header class="hero">
    <div class="hero-photo" role="img" aria-label="Photograph of misty Scottish highland mountains with moorland in the foreground"></div>
    <div class="portrait" role="img" aria-label="Portrait photograph of the coach in a tweed jacket and white shirt"></div>
    <h1 class="series-title">Glenmoor Vale Executive Development Workshop Series – <b>First Thursdays</b></h1>
    <div class="coach-name">Ian Mercer</div>
    <div class="coach-rule"></div>
    <div class="coach-title">Certified Professional Business Coach</div>
    <p class="tagline">A positive, fresh, results-driven approach for businesses to increase profits by building confidence, command and control in owners and executives.</p>
  </header>
  <svg class="swoosh" viewBox="0 0 850 140" preserveAspectRatio="none" aria-hidden="true">
    <path d="M0 25 C180 55 420 110 850 95 L850 140 L0 140 Z" fill="var(--sage)"/>
    <path d="M0 22 C200 60 430 122 850 112 L850 140 L0 140 Z" fill="var(--paper)"/>
  </svg>

  <section class="intro">
    <p>We will use proven leadership and business strategies to improve work-life balance, buy-in, and company value. Here’s your opportunity to meet with other like-minded business owners and executives once a month in a private and confidential setting.</p>
    <p>We’ve got nine subject areas planned, and while they are all powerful, we will shift from high-level strategy topics to “where the rubber meets the road” topics.</p>
  </section>

  <section class="includes">
    <h2>Monthly Workshop Series Includes:</h2>
    <div class="include-item"><strong>3-Hour Intensive Workshop</strong>High-energy, creative sessions with engaging and relevant business topics, peer group advisory board (master mind), and networking (9am - 12pm, dates above)</div>
    <div class="include-item"><strong>90-minute one-on-one coaching session</strong>to help you absorb and apply the revelations from the group sessions to your own business (mutually scheduled)</div>
  </section>

  <section class="fine-print">
    <p>Participation and trust is vital to your investment; no holding back. Due to the confidential nature of the intensive workshops, all participants will sign a confidentiality agreement. Additionally, we will only allow one company per industry to be represented.</p>
    <p class="venue">All monthly Intensive Workshops will be 9am - 12pm on the dates at Kiln Street Coworking at 210 Foundry Lane, Millbrook NC 27000</p>
  </section>

  <p class="price">$395/month or $295/month with a 6-month or greater commitment</p>

  <div class="member-badge" role="img" aria-label="Professional association member badge"></div>

  <ul class="schedule">
    <li><span class="session"><b>SEP 7</b> – My Company Owns Me</span><span class="summary">What a CEO should and should not do</span></li>
    <li><span class="session"><b>OCT 5</b> – Taking Vision / Mission / Values</span><span class="summary">Down To The Molecular Level Of Your Company</span></li>
    <li><span class="session"><b>NOV 2</b> – People Problems</span><span class="summary">The biggest waste of time and money for every small business</span></li>
    <li><span class="session"><b>Dec 7</b> – Value Delivery Systems</span><span class="summary">Re-think everything you think you know about creating value</span></li>
    <li><span class="session"><b>Jan 4, 2018</b> – Rally Your Team Around A Goal</span><span class="summary">How to create a meaningful company goal and rally the troops around it</span></li>
    <li><span class="session"><b>Feb 1</b> – Building Your Executive Leadership Team</span><span class="summary">You can’t succeed without one</span></li>
    <li><span class="session"><b>Mar 1</b> – Improve Your Outside Sales Efforts</span><span class="summary">Help your sales force to be busy AND successful</span></li>
    <li><span class="session"><b>Apr 5</b> – Every Brain In The Game</span><span class="summary">Engage your team and build a strong culture</span></li>
    <li><span class="session"><b>May 3</b> – Repeatable Processes</span><span class="summary">Coach your employees how to get predictable results every time</span></li>
    <li><span class="session"><b>Jun 7</b> – Finding and Filling Profit Holes</span><span class="summary">Most small businesses waste more money than they profit</span></li>
    <li><span class="session"><b>Jul 12</b> – Put Your Payroll On A Diet</span><span class="summary">Why waste happens, what to do about it and how it helps everyone</span></li>
    <li><span class="session"><b>Aug 2</b> – Truly, How Effective Are You With This Whole “Leadership” Thing?</span></li>
  </ul>

  <div class="register">To register, go to <b>glenmoorvale.com/exec-dev</b> and click the registration link</div>

  <div class="footer-band"></div>
  <footer class="footer">
    <div class="footer-name"><b>IAN MERCER,</b> Certified Professional Business Coach</div>
    <ul class="contact">
      <li><svg viewBox="0 0 10 10"><path d="M2 0 L4 2 L3 3.5 Q4.5 6 6.5 7 L8 6 L10 8 L8.5 10 Q2 9 0 1.5 Z"/></svg>(555)014-2290</li>
      <li><svg viewBox="0 0 10 10"><path d="M0 2 H10 V8 H0 Z"/></svg>ian@glenmoorvale.com</li>
      <li><svg viewBox="0 0 10 10"><circle cx="5" cy="5" r="4.5"/></svg>glenmoorvale.com</li>
    </ul>
    <div class="brand"><span class="brand-dot"></span>Glenmoor Vale</div>
  </footer>
</main>
</body>
</html>
```